Business Telephone Service Brochure

I need a brochure designed to help sell our VoIP service. The brochure needs to be clean, attention getting, professional and have 3 key areas of information (Key Features, Benefits & Service Plans). Here is an idea of what we are looking for https://www.artflockly.com/design/52930487. Need to also include how much the customer could save. See this for an example https://42mockups.com/postcard-flyer-design/contests/voip-sales-flyer-template-replicate-attached-358209. The Service Plan section needs to allow room for two types of plans. One plan includes the phone and has a 12, 24 and 36 month option. Each term (12,24,36) will have its own monthly cost per device. The second service option is no-commitment monthly with a single per month price per device. The included features section should allow for up to 16 features to be listed. The benefits should allow for 4-6 benefits to be listed. Also include room for Logo, business address, website, phone number and email.

Target Market(s)

Small to medium business with 1-100 employees.

Industry/Entity Type

Telecommunications

Font styles to use
Serif

Colors

Designer to choose colors to be used in the design.

Requirements
Must have
• Key Feature, Benefits and Service Plans (i.e. Pricing). Company logo, phone, email and website. Must have "Save up to x%!" and catch attention.
Nice to have
• Limited colors. I am not setting a hard limit, please take the liberty to do what you feel is needed. Just keep in mind we want it to be clean, professional and attention getting without being to flashy or obnoxious.
Should not have
• Nothing busy or distracting.

```html
<!DOCTYPE html>
<html lang="en">
<head>
<meta charset="utf-8">
<title>nexa – Business Telephone Service Flyer</title>
<link href="https://fonts.googleapis.com/css2?family=Montserrat:wght@600;700;800&family=Quicksand:wght@400;500;600;700&display=swap" rel="stylesheet">
<style>
  :root{
    --stage:#e4e5e8;
    --navy:#2f2f8e;
    --navy-deep:#0b1440;
    --ink:#0a0b12;
    --sky:#3fb2e2;
    --term-12:#4c9ed4;
    --term-24:#5d66b6;
    --term-36:#3c3d98;
    --mist:#eef0f3;
    --slate:#d9dce2;
    --charcoal:#2b2c30;
    --text:#2a2c38;
    --alert:#d22222;
    --white:#ffffff;
    --display:"Montserrat", Arial, sans-serif;
    --body:"Quicksand", Arial, sans-serif;
  }
  *{box-sizing:border-box;margin:0;padding:0}
  html,body{width:1200px;height:1000px;overflow:hidden;background:var(--stage)}
  .canvas{position:relative;width:1200px;height:1000px;font-family:var(--body);color:var(--text)}
  .page{position:absolute;top:120px;width:520px;height:760px;background:var(--white);overflow:hidden;box-shadow:0 6px 24px rgba(0,0,0,.18)}
  .page--front{left:50px}
  .page--back{left:630px}

  /* brand */
  .brand{text-align:center;color:var(--navy)}
  .brand__name{font-family:var(--display);font-weight:800;font-size:58px;line-height:1;letter-spacing:-1px}
  .brand__tag{font-size:9px;font-weight:600;letter-spacing:.5px;margin-top:4px}

  /* front */
  .front__head{position:absolute;top:0;left:0;width:100%;height:112px;background:var(--mist);padding-top:24px}
  .front__notch{position:absolute;top:110px;left:50%;transform:translateX(-50%);width:0;height:0;border-left:14px solid transparent;border-right:14px solid transparent;border-top:12px solid var(--mist);z-index:2}
  .hero{position:absolute;top:112px;left:0;width:100%;height:300px;background:
      radial-gradient(ellipse at 70% 35%, rgba(70,130,255,.55), transparent 55%),
      linear-gradient(160deg,#0d1a55,var(--navy-deep) 70%)}
  .hero__offer{position:absolute;left:40px;top:96px;color:var(--white);font-weight:500}
  .hero__line{font-size:34px;letter-spacing:.5px}
  .hero__value{font-size:64px;font-weight:700;color:#c9d6ff;margin-left:60px;line-height:1}
  .hero__cut{position:absolute;left:0;top:372px;width:520px;height:40px;display:block}

  .benefits__title{position:absolute;top:418px;width:100%;text-align:center;font-family:var(--display);font-weight:800;font-size:30px;color:var(--navy)}
  .benefits{position:absolute;top:470px;left:20px;width:480px;height:190px;background:var(--mist);display:grid;grid-template-columns:1fr 1fr;grid-auto-rows:1fr;padding:6px 10px}
  .benefits__rail{position:absolute;left:30px;top:20px;width:2px;height:150px;background:var(--navy)}
  .benefit{display:flex;flex-direction:column;align-items:center;justify-content:center;text-align:center;font-size:14px;font-weight:500;line-height:1.15}
  .benefit__icon{width:30px;height:30px;border-radius:50%;background:var(--navy);display:flex;align-items:center;justify-content:center;margin-bottom:4px}
  .benefit__icon svg{width:16px;height:16px}

  .front__contact{position:absolute;top:668px;left:0;width:100%;display:flex;justify-content:center;gap:30px;font-size:15px;font-weight:600;color:var(--text)}
  .front__band{position:absolute;bottom:0;left:0;width:100%;height:52px;background:var(--navy);color:var(--white);display:flex;align-items:center;padding-left:40px;font-size:17px;font-weight:600;gap:8px}
  .dot-icon{display:inline-flex;width:16px;height:16px;border-radius:50%;background:currentColor;align-items:center;justify-content:center;flex:none}
  .dot-icon svg{width:10px;height:10px}

  /* back */
  .back__band{position:absolute;top:0;left:0;width:100%;height:36px;background:var(--navy)}
  .features{position:absolute;top:36px;left:0;width:100%;height:384px;background:
      radial-gradient(ellipse at 55% 40%, #2b2e3c, var(--ink) 65%);color:var(--white)}
  .features__pill{position:absolute;top:18px;left:50%;transform:translateX(-50%);border:2px solid var(--white);background:var(--navy);border-radius:18px;padding:4px 22px;font-size:14px;font-weight:600;letter-spacing:.5px;white-space:nowrap}
  .features__list{position:absolute;top:66px;left:56px;list-style:none;font-size:17px;font-weight:500;line-height:21.5px}
  .features__list li{display:flex;align-items:center;gap:10px}
  .features__list li::before{content:"";width:10px;height:10px;border-radius:50%;border:2px solid var(--white);flex:none}
  .features__notch{position:absolute;top:419px;left:50%;transform:translateX(-50%);border-left:16px solid transparent;border-right:16px solid transparent;border-top:14px solid var(--ink);z-index:2}

  .plans{position:absolute;top:420px;left:0;width:100%;height:230px;background:var(--mist)}
  .plans__title{position:absolute;top:30px;left:16px;width:150px;height:22px;display:flex;align-items:center;font-family:var(--display);font-weight:700;font-size:17px;color:var(--navy);white-space:nowrap}
  .plans__grid{position:absolute;top:30px;left:172px;display:grid;grid-template-columns:repeat(4,80px);grid-template-rows:22px 40px 40px;gap:2px}
  .plans__head{font-size:9px;font-weight:700;color:var(--white);display:flex;align-items:center;justify-content:center;text-transform:uppercase;white-space:nowrap}
  .plans__cell{display:flex;align-items:center;justify-content:center;color:var(--white);font-family:var(--display);font-weight:700;font-size:16px}
  .c-m{background:var(--sky)} .c-12{background:var(--term-12)} .c-24{background:var(--term-24)} .c-36{background:var(--term-36)}
  .plans__rows{position:absolute;top:54px;left:16px;width:154px;display:grid;grid-template-rows:40px 40px;gap:2px}
  .plans__label{background:var(--slate);font-size:10px;font-weight:600;display:flex;align-items:center;padding-left:8px;line-height:1.2}
  .plans__notes{position:absolute;top:146px;left:20px;right:20px;font-size:9px;font-weight:600;line-height:1.4}
  .plans__notes em{color:var(--alert);font-style:normal}

  .back__foot{position:absolute;top:650px;left:0;width:100%;height:110px}
  .back__logo{position:absolute;left:30px;top:12px}
  .back__logo .brand__name{font-size:44px}
  .back__logo .brand__tag{font-size:7px}
  .back__foot-band{position:absolute;left:0;bottom:0;width:300px;height:22px;background:var(--navy)}
  .back__contacts{position:absolute;right:0;top:0;width:220px;height:110px;background:var(--charcoal);color:var(--white);padding:18px 0 0 22px;font-size:15px;font-weight:500;line-height:24px}
  .back__contacts div{display:flex;align-items:center;gap:8px}
  .back__contact-tag{position:absolute;right:220px;top:14px;background:var(--term-24);color:var(--white);padding:4px 14px;font-size:14px;font-weight:600}
</style>
</head>
<body>
<main class="canvas">

  <section class="page page--front" aria-label="Flyer front: offer and benefits">
    <header class="front__head">
      <div class="brand">
        <div class="brand__name">nexa</div>
        <div class="brand__tag">Internet-Telephone-Security-Networking</div>
      </div>
    </header>
    <div class="front__notch"></div>

    <div class="hero" role="img" aria-label="Glowing blue circuit board traces on dark navy background">
      <div class="hero__offer">
        <div class="hero__line">SAVE UP TO</div>
        <div class="hero__value">X%!</div>
      </div>
    </div>
    <svg class="hero__cut" viewBox="0 0 520 40" preserveAspectRatio="none">
      <polygon points="0,40 520,0 520,40" fill="#ffffff"/>
    </svg>

    <h2 class="benefits__title">BENEFITS OF “nexa”</h2>
    <div class="benefits">
      <span class="benefits__rail"></span>
      <div class="benefit">
        <span class="benefit__icon"><svg viewBox="0 0 24 24"><path fill="#fff" d="M6.6 10.8a15 15 0 0 0 6.6 6.6l2.2-2.2c.3-.3.7-.4 1-.2 1.1.4 2.3.6 3.6.6.6 0 1 .4 1 1V20c0 .6-.4 1-1 1A17 17 0 0 1 3 4c0-.6.4-1 1-1h3.5c.6 0 1 .4 1 1 0 1.3.2 2.5.6 3.6.1.3 0 .7-.2 1z"/></svg></span>
        No expensive onsite<br>telephone equipment
      </div>
      <div class="benefit">
        <span class="benefit__icon"><svg viewBox="0 0 24 24"><path fill="none" stroke="#fff" stroke-width="2.4" d="M3 7h5l8 10h5M3 17h5l8-10h5"/></svg></span>
        Easily scale up or down<br>and needs change
      </div>
      <div class="benefit">
        <span class="benefit__icon"><svg viewBox="0 0 24 24"><path fill="#fff" d="M4 20h4v-6H4zm6 0h4V9h-4zm6 0h4V4h-4z"/></svg></span>
        Increase reliability
      </div>
      <div class="benefit">
        <span class="benefit__icon"><svg viewBox="0 0 24 24"><rect x="3" y="7" width="18" height="10" rx="2" fill="none" stroke="#fff" stroke-width="2"/></svg></span>
        Free telephone/email support
      </div>
      <div class="benefit">
        <span class="benefit__icon"><svg viewBox="0 0 24 24"><path fill="#fff" d="M12 20l-7-7h4V4h6v9h4z"/></svg></span>
        Lower monthly cost
      </div>
      <div class="benefit">
        <span class="benefit__icon"><svg viewBox="0 0 24 24"><circle cx="12" cy="8" r="4" fill="#fff"/><path fill="#fff" d="M4 21a8 8 0 0 1 16 0z"/></svg></span>
        Easy self-administration
      </div>
    </div>

    <div class="front__contact">
      <span>Contact Us:</span>
      <span>www.nexavoice.net</span>
      <span>email@nexavoice.net</span>
    </div>
    <footer class="front__band">
      <span class="dot-icon"><svg viewBox="0 0 24 24"><path fill="#2f2f8e" d="M6.6 10.8a15 15 0 0 0 6.6 6.6l2.2-2.2 5 1.5V21A17 17 0 0 1 3 4h4.5l1.5 5z"/></svg></span>
      0123456789
    </footer>
  </section>

  <section class="page page--back" aria-label="Flyer back: features and service plans">
    <div class="back__band"></div>
    <div class="features">
      <div class="features__pill">INCLUDED KEY FEATURES</div>
      <ul class="features__list">
        <li>Unlimited local and long distance calling</li>
        <li>HD Voice</li>
        <li>Business SMS/Text Messaging</li>
        <li>Personal and Shared Voicemail Boxes</li>
        <li>Audio Conferencing</li>
        <li>Intercom</li>
        <li>Mobile App</li>
        <li>Auto Attendant/Interactive Voice Routing</li>
        <li>Free web or email fax</li>
        <li>Web admin portal</li>
        <li>Music On Hold – Customizable</li>
        <li>Simultaneous ring / follow-me</li>
        <li>Redundancy/Failover – Never miss a call</li>
      </ul>
    </div>
    <div class="features__notch"></div>

    <div class="plans">
      <h2 class="plans__title">SERVICE PLANE</h2>
      <div class="plans__grid">
        <div class="plans__head c-m">Monthly</div>
        <div class="plans__head c-12">12 Month Term</div>
        <div class="plans__head c-24">24 Month Term</div>
        <div class="plans__head c-36">36 Month Term</div>
        <div class="plans__cell c-m">$21.95</div>
        <div class="plans__cell c-12"></div>
        <div class="plans__cell c-24"></div>
        <div class="plans__cell c-36"></div>
        <div class="plans__cell c-m"></div>
        <div class="plans__cell c-12">$24.95</div>
        <div class="plans__cell c-24">$22.95</div>
        <div class="plans__cell c-36">$20.95</div>
      </div>
      <div class="plans__rows">
        <div class="plans__label">*Phone service only<br>(Phone sold separately)</div>
        <div class="plans__label">Service + Veltro V23 Phone</div>
      </div>
      <p class="plans__notes">
        <em>*</em>For monthly service you may purchase the Veltro V23 phone for $65 each, less taxes and shipping.<br>
        <em>**</em>Veltro V23 phones are rented and due upon cancellation. Customer pays return shipping.
      </p>
    </div>

    <footer class="back__foot">
      <div class="back__logo brand">
        <div class="brand__name">nexa</div>
        <div class="brand__tag">Internet-Telephone-Security-Networking</div>
      </div>
      <div class="back__contact-tag">Contact Us:</div>
      <div class="back__contacts">
        <div><span class="dot-icon"><svg viewBox="0 0 24 24"><path fill="#2b2c30" d="M6.6 10.8a15 15 0 0 0 6.6 6.6l2.2-2.2 5 1.5V21A17 17 0 0 1 3 4h4.5l1.5 5z"/></svg></span>0123456789</div>
        <div><span class="dot-icon"><svg viewBox="0 0 24 24"><rect x="4" y="7" width="16" height="10" fill="#2b2c30"/></svg></span>email@nexavoice.net</div>
        <div><span class="dot-icon"><svg viewBox="0 0 24 24"><circle cx="12" cy="12" r="6" fill="none" stroke="#2b2c30" stroke-width="3"/></svg></span>www.nexavoice.net</div>
      </div>
      <div class="back__foot-band"></div>
    </footer>
  </section>

</main>
</body>
</html>
```